K & R Ground Works. Business card design

We need a business card designed for a new business. We have a bulldozer and tractor service. We clear land and make wildlife food plots. We provide disking, bush hogging, and site prep services.
I have attached an image of a business card that I like and would like my business cards to look similar.

Target Market(s)

anyone needing bulldozer and/or tractor services

Industry/Entity Type

Business

Contact Information for Business Card

K & R Ground Works, Operated by 7-T-Ranch
Dale Whitcomb
601-555-0148
dwk4821@mailbarn.example

Font styles to use
Sans Serif

Colors

Designer to choose colors to be used in the design.

Requirements
Must have
• image of tractor and bulldozer
• Land Clearing
• Wildlife food plots
• Bush Hogging
• Disking
• Site prep
Nice to have
• i have included a image of a business card that i like. I would like mine to be similar.

```html
<!DOCTYPE html>
<html lang="en">
<head>
<meta charset="utf-8">
<title>K &amp; R Ground Works – Business Card</title>
<link rel="stylesheet" href="https://fonts.googleapis.com/css2?family=Roboto:wght@400;700&family=Open+Sans:wght@700&display=swap">
<style>
  :root {
    --backdrop: #e9e4dc;
    --card-white: #ffffff;
    --divider-grey: #a9a9a9;
    --brand-brown: #6b3a12;
    --tagline-grey: #6b6b6b;
    --rule-grey: #9a9a9a;
    --accent-orange: #e0771c;
    --photo-dark: #1b1f17;
    --photo-mid: #2e3a22;
    --tractor-orange: #c9552a;
    --dozer-yellow: #b8a43a;
    --foliage: #4f6b2e;
    --text-light: #ffffff;
  }
  * { box-sizing: border-box; margin: 0; padding: 0; }
  html, body {
    width: 1200px; height: 900px; overflow: hidden;
    background: var(--backdrop);
  }
  .canvas { position: relative; width: 1200px; height: 900px; }
  .card {
    position: absolute; left: 320px; width: 584px; height: 360px;
    background: var(--card-white);
    box-shadow: 3px 4px 8px rgba(0,0,0,0.35);
    overflow: hidden;
  }
  .card--front { top: 88px; }
  .card--back { top: 478px; }
  .card__header {
    position: absolute; left: 0; top: 0; width: 100%; height: 118px;
    background: var(--card-white);
  }
  .brand-mark {
    position: absolute; left: 38px; top: 36px; width: 38px; height: 38px;
    border-radius: 50%; background: var(--accent-orange);
  }
  .brand-name {
    position: absolute; left: 116px; top: 36px;
    font-family: "Roboto", Arial, sans-serif; font-weight: 700;
    font-size: 27px; letter-spacing: -0.3px;
    color: var(--brand-brown); white-space: nowrap;
  }
  .brand-tagline {
    position: absolute; left: 118px; top: 68px; width: 338px;
    display: flex; align-items: center; gap: 10px;
    font-family: "Open Sans", Arial, sans-serif; font-weight: 700;
    font-size: 17px; color: var(--tagline-grey); white-space: nowrap;
  }
  .brand-tagline::before, .brand-tagline::after {
    content: ""; flex: 1; height: 1px; background: var(--rule-grey);
  }
  .card__divider {
    position: absolute; left: 0; top: 116px; width: 100%; height: 5px;
    background: var(--divider-grey);
  }
  .card__photo {
    position: absolute; left: 0; top: 121px; width: 100%; height: 239px;
  }
  .card__photo--tractor {
    background:
      linear-gradient(90deg, var(--photo-dark) 0%, var(--photo-mid) 38%, rgba(46,58,34,0) 60%),
      linear-gradient(160deg, var(--foliage) 0%, var(--tractor-orange) 55%, #7a3a1c 100%);
  }
  .card__photo--dozer {
    background:
      linear-gradient(90deg, var(--photo-dark) 0%, #263021 35%, rgba(38,48,33,0) 58%),
      linear-gradient(170deg, var(--foliage) 0%, #5b5a3a 50%, var(--dozer-yellow) 85%, #3e5a24 100%);
  }
  .contact {
    position: absolute; left: 38px; top: 195px;
    font-family: "Roboto", Arial, sans-serif; color: var(--text-light);
  }
  .contact__name { font-weight: 700; font-size: 23px; margin-bottom: 10px; }
  .contact__line {
    display: flex; align-items: center; gap: 6px;
    font-size: 17px; line-height: 24px;
  }
  .contact__icon { width: 14px; height: 12px; fill: var(--text-light); }
  .services {
    position: absolute; left: 38px; top: 175px; list-style: none;
    font-family: "Roboto", Arial, sans-serif; font-size: 18px;
    line-height: 23.5px; color: var(--text-light);
  }
</style>
</head>
<body>
<main class="canvas">
  <section class="card card--front">
    <header class="card__header">
      <span class="brand-mark"></span>
      <h1 class="brand-name">K &amp; R GROUND WORKS</h1>
      <p class="brand-tagline">OPERATED BY 7-T-RANCH</p>
    </header>
    <div class="card__divider"></div>
    <div class="card__photo card__photo--tractor" role="img" aria-label="Photo of an orange tractor with front loader bucket in brush"></div>
    <div class="contact">
      <p class="contact__name">Dale Whitcomb</p>
      <p class="contact__line">
        <svg class="contact__icon" viewBox="0 0 14 12" aria-hidden="true"><path d="M1 3 Q7 -1 13 3 L12 5 L9.5 4.2 L9.3 3 Q7 2.3 4.7 3 L4.5 4.2 L2 5 Z M3 6 L11 6 L12 11 L2 11 Z"/></svg>
        601-555-0148
      </p>
      <p class="contact__line">
        <svg class="contact__icon" viewBox="0 0 14 12" aria-hidden="true"><path d="M1 2 H13 V10 H1 Z M1.8 2.8 L7 7 L12.2 2.8" stroke="#1b1f17" stroke-width="1"/></svg>
        dwk4821@mailbarn.example
      </p>
    </div>
  </section>

  <section class="card card--back">
    <header class="card__header">
      <span class="brand-mark"></span>
      <h2 class="brand-name">K &amp; R GROUND WORKS</h2>
      <p class="brand-tagline">OPERATED BY 7-T-RANCH</p>
    </header>
    <div class="card__divider"></div>
    <div class="card__photo card__photo--dozer" role="img" aria-label="Photo of a yellow bulldozer clearing brush by a tree line"></div>
    <ul class="services">
      <li>Land Clearing</li>
      <li>Wildlife food plots</li>
      <li>Bush Hogging</li>
      <li>Disking</li>
      <li>Site prep</li>
    </ul>
  </section>
</main>
</body>
</html>
```